I have a new startup... www.hirewithplindle.com
An issue Im running into is when people create profiles there banner images are getting messed up. So instead I would like anywhere to 10-15 banners created as stock banners for my site the people signing up need to choose from so the website looks more in uniform. The site contains graphic designers, photographers, & videographers so maybe some banners can be patterns of a camera outline or graphic design tools etc. Need really clean and sleek looking banners that these people can pick from that will make sense.
I will attach my logo if you want to do a cool "Plindle" pattern design as a banner.
Banner sizes 2000px by 560px.

If you have any questions please let me know.

```html
<!DOCTYPE html>
<html lang="en">
<head>
<meta charset="utf-8">
<title>Plindle – Find Creative Pros</title>
<link rel="stylesheet" href="https://fonts.googleapis.com/css2?family=Roboto:wght@300;700;900&family=Roboto+Condensed:wght@400&display=swap">
<style>
  :root {
    --ink: #050505;
    --brand: #c9472a;
    --glow: #e0501c;
    --glow-deep: #6e1d08;
    --text: #ffffff;
  }
  * { margin: 0; padding: 0; box-sizing: border-box; }
  html, body {
    width: 1200px;
    height: 336px;
    overflow: hidden;
    background: var(--ink);
  }
  .banner {
    position: relative;
    width: 1200px;
    height: 336px;
    overflow: hidden;
    background:
      radial-gradient(ellipse 420px 90px at 820px 250px, rgba(224, 80, 28, 0.38), transparent 70%),
      radial-gradient(ellipse 300px 70px at 1050px 150px, rgba(224, 80, 28, 0.22), transparent 70%),
      radial-gradient(ellipse 520px 120px at 520px 320px, rgba(224, 80, 28, 0.30), transparent 70%),
      radial-gradient(ellipse 260px 60px at 1150px 320px, rgba(110, 29, 8, 0.55), transparent 70%),
      var(--ink);
  }
  .light-streaks {
    position: absolute;
    inset: 0;
    background: linear-gradient(160deg, transparent 40%, rgba(224, 80, 28, 0.12) 62%, transparent 80%);
  }
  .creative-tools {
    position: absolute;
    left: 36px;
    top: 14px;
    width: 545px;
    height: 322px;
    border-radius: 10px;
    background:
      radial-gradient(ellipse 110px 70px at 220px 170px, rgba(240, 140, 60, 0.55), transparent 75%),
      radial-gradient(ellipse 80px 60px at 290px 190px, rgba(70, 150, 90, 0.5), transparent 75%),
      radial-gradient(ellipse 140px 120px at 90px 210px, rgba(60, 60, 60, 0.8), transparent 75%),
      radial-gradient(ellipse 140px 110px at 250px 90px, rgba(45, 45, 45, 0.8), transparent 75%),
      radial-gradient(ellipse 120px 80px at 420px 230px, rgba(180, 150, 110, 0.35), transparent 75%);
  }
  .brand-name {
    position: absolute;
    left: 612px;
    top: 42px;
    font-family: "Roboto", sans-serif;
    font-weight: 900;
    font-size: 90px;
    line-height: 1;
    letter-spacing: -1px;
    color: var(--brand);
    text-transform: uppercase;
  }
  .tagline {
    position: absolute;
    left: 611px;
    top: 140px;
    font-family: "Roboto", sans-serif;
    font-weight: 300;
    font-size: 45px;
    line-height: 1;
    color: var(--text);
  }
  .subline {
    position: absolute;
    left: 612px;
    top: 199px;
    font-family: "Roboto Condensed", sans-serif;
    font-weight: 400;
    font-size: 37px;
    line-height: 1;
    color: var(--text);
  }
  .site-url {
    position: absolute;
    left: 609px;
    top: 258px;
    font-family: "Roboto", sans-serif;
    font-weight: 700;
    font-size: 36px;
    line-height: 1;
    letter-spacing: 3.4px;
    color: var(--text);
  }
  .pointer-icon {
    position: absolute;
    left: 1134px;
    top: 270px;
    width: 40px;
    height: 46px;
  }
</style>
</head>
<body>
  <main class="banner">
    <div class="light-streaks" role="img" aria-label="Abstract glowing orange light streaks on black"></div>
    <div class="creative-tools" role="img" aria-label="Illustration of a film camera, photo camera on tripod, drawing tablet, brushes, coffee mug and sketchbooks"></div>

    <div class="brand-name">Plindle</div>
    <p class="tagline">Find Creative Pros</p>
    <p class="subline">Work with local professionals.</p>
    <p class="site-url">www.hirewithplindle.com</p>

    <svg class="pointer-icon" viewBox="0 0 40 46" aria-hidden="true">
      <path d="M2 2 L2 38 L11 29 L18 44 L25 41 L18 27 L31 27 Z" fill="#ffffff" stroke="#050505" stroke-width="2" stroke-linejoin="round"/>
    </svg>
  </main>
</body>
</html>
```